Real Estate Search Site Re-Design of 2 Pages

Looking for designs to optimize 2 pages of our current site design. Our site allows users to find properties to purchase or rent.

Basically there are 4 panes
1. The top red one where you actually type in what you''re looking for.
2. The map pane that shows the properties
3. The scrollable results pane.
4. Property details pane.

A typical search would go like this:
1. User fills in their search criteria in the top pane in red. Clicks Find Homes
2. Site updates the map with properties plotted that fit the criteria. Site also populates the results pane at the bottom. Site shows the most newest property that fits the search criteria on the right.
3. User will scroll through the results pane or the map and click a property.
4. Site will update the property details pane with information on the selected property.

Search/Results Page
This main page needs a search form area, a results area, an area to display details of a property selected, a map to show results, and an area to display a real estate agent's information. The design must be full-screen to use all the space on the screen. All information should fit on a 1366x768 screen size. Please see sample screen shot.

Property Details Page
This one can be fixed width of 978px. This page needs all the elements that are displayed in the sample PNG file. Ideally, we want to be able to see all important information without scrolling on a 1366x768 screen. The important information in this size are Pictures with controls, address, bedrooms, bathrooms, square feet, square feet of the lot, days on market, agent information, and buttons to request a showing or get more information.

Our Goal:
Our goal is to get create a different way to display the data in an effective way. We want different ways to show the search results, maybe a vertical, scrolling list of property information with pictures. Or even a horizontal scrolling results pane. It must contain:

1. A map of the results
2. A way to scroll through the search results (like we have currently in case someone wants to search/sort bedrooms or square footage)
3. A way to view details of the property
4. A way to display agent information/picture

There's a lot of good design work coming through. Thank you.

Perhaps review some other real estate sales sites for ideas on pane configuration. Example site links:
http://www.brovenly.com/homes/for_sale/?gclid=QmTr8k2-xw7HJd3P9Lq0VnE5ZB (brovenly.com)
http://www.pemoda.com/?sem=1.2.1.5.7.1.0.14&gclid=ZKwp42h-ty8NGRmX5BqeuLcHTD (Pemoda.com)
http://www.quivrent.com/map_search/results/i/ (quivrent.com)

Our goal for the redesign is to display the data in a more effective way. Either with a better flow, more pictures, more information, smoother search process. Please see the updated brief for details. The main idea is to show the data in the most effective way possible.

Project Deadline Extended
Reason: Still looking at different ideas for the search results. We are still open for fresh ideas.

Industry/Entity Type

Real Estate

Font styles to use
Sans Serif

Colors
eb1f27

```html
<!DOCTYPE html>
<html lang="en">
<head>
<meta charset="utf-8">
<title>Real Estate Company – Search</title>
<link href="https://fonts.googleapis.com/css2?family=Lato:wght@400;700&family=Roboto+Condensed:wght@400&display=swap" rel="stylesheet">
<style>
:root{
  --brand:#eb1f27;
  --brand-dark:#c10f15;
  --ink:#222;
  --muted:#555;
  --page:#f1f1f1;
  --panel:#ffffff;
  --line:#d8d8d8;
  --night:#0b0b0d;
  --orange:#f7941d;
}
*{box-sizing:border-box;margin:0;padding:0}
html,body{width:1200px;height:1012px;overflow:hidden}
body{position:relative;background:#fff;font-family:"Lato",sans-serif;color:var(--ink)}
.abs{position:absolute}
.top-rule{left:0;top:0;width:1200px;height:2px;background:#333}
.phone{left:644px;top:9px;font-family:"Roboto Condensed",sans-serif;font-size:21px;color:#333;white-space:nowrap}
.phone .free{color:var(--brand);margin-left:10px}
.locale{left:895px;top:0;width:159px;height:38px;background:#222;border-radius:0 0 4px 4px;color:#fff;font-size:12px;display:flex;align-items:center;padding-left:13px;gap:6px}
.locale .flag{width:19px;height:13px;background:#3b4a8c;border:1px solid #c33}
.locale .sep{width:1px;height:18px;background:#555;margin:0 6px}
.brand{left:145px;top:43px;font-size:28px;color:var(--brand);font-weight:400}
.nav{top:57px;font-size:13px;color:#111;letter-spacing:.2px}
.page{left:0;top:141px;width:1200px;height:569px;background:var(--page)}
.search{left:145px;top:94px;width:909px;height:47px;background:linear-gradient(#f0262e,#d4121a);border-radius:5px 5px 0 0;border-bottom:3px solid #b70d13}
.field{top:103px;height:29px;background:#fff;border:1px solid #ccc;font-size:14px;color:#444;display:flex;align-items:center;padding-left:9px;justify-content:space-between;padding-right:9px}
.lbl{top:109px;color:#fff;font-size:14px}
.go{left:996px;top:103px;width:30px;height:29px;background:var(--orange);display:flex;align-items:center;justify-content:center}
.map{left:145px;top:141px;width:612px;height:371px;background:linear-gradient(135deg,#e8e4dc,#ddd8cc 55%,#e6e1d6)}
.detail{left:757px;top:141px;width:297px;height:371px;background:var(--panel);border-right:1px solid var(--line)}
.photo{left:790px;top:165px;width:235px;height:155px;background:linear-gradient(160deg,#7c8a6a,#3a3f33 55%,#6d5a44)}
.arrow{top:218px;width:30px;height:30px;border-radius:50%;background:rgba(60,60,60,.55)}
.d-title{left:757px;top:331px;width:297px;text-align:center;font-size:15px;color:#333}
.d-line{left:790px;font-size:11px;color:#555}
.d-line b{color:#333}
.btn{top:467px;height:22px;background:linear-gradient(#f0262e,#c8111a);border:1px solid #a00;border-radius:3px;color:#fff;font-size:12px;display:flex;align-items:center;justify-content:center}
.results{left:145px;top:514px;width:909px;height:155px;background:#fff;border:1px solid var(--line)}
table{border-collapse:collapse;width:896px;table-layout:fixed}
th{background:#111;color:#fff;font-size:15px;font-weight:700;height:32px;border-right:1px solid #444}
td{height:24.8px;font-family:"Roboto Condensed",sans-serif;font-size:12px;color:#222;border-right:1px solid var(--line);border-bottom:1px solid #e6e6e6;padding-left:9px;background:linear-gradient(#fff,#efefef)}
td.c{text-align:center;padding-left:0}
tr.active td{background:linear-gradient(#f0262e,#cc1219);color:#fff}
.scroll{left:1041px;top:546px;width:13px;height:122px;background:#eee}
.scroll i{position:absolute;left:3px;top:16px;width:7px;height:28px;background:#ccc;border-radius:4px}
.footer{left:0;top:710px;width:1200px;height:302px;background:var(--night)}
.f-h{top:743px;font-size:20px;color:#fff}
.about{left:147px;top:777px;width:600px;font-size:12.5px;line-height:21px;color:#bbb}
.social{top:782px;width:34px;height:34px;border-radius:50%;background:#fff;color:#111;font-size:9px;display:flex;align-items:center;justify-content:center}
.skyline{left:0;top:845px;width:1200px;height:167px;background:linear-gradient(#0b0b0d,#2a2a2c 45%,#5a5a5c)}
</style>
</head>
<body>
<div class="abs top-rule"></div>
<div class="abs phone">+31-20-4827150<span class="free">FREE CALL</span></div>
<div class="abs locale"><span class="flag"></span>EN
<svg width="10" height="6" viewBox="0 0 10 6"><path d="M1 1l4 4 4-4" stroke="#fff" stroke-width="1.6" fill="none"/></svg>
<span class="sep"></span>NZD ($)
<svg width="10" height="6" viewBox="0 0 10 6"><path d="M1 1l4 4 4-4" stroke="#fff" stroke-width="1.6" fill="none"/></svg></div>
<div class="abs brand">Real Estate Company</div>
<div class="abs nav" style="left:752px">COMMUNITIES</div>
<div class="abs nav" style="left:872px">LOCATIONS</div>
<div class="abs nav" style="left:973px">CONTACT US</div>

<div class="abs page"></div>

<div class="abs search"></div>
<div class="abs field" style="left:173px;width:196px">Location</div>
<div class="abs field" style="left:380px;width:153px">Type<svg width="11" height="7" viewBox="0 0 11 7"><path d="M1 1l4.5 4.5L10 1" stroke="#222" stroke-width="1.8" fill="none"/></svg></div>
<div class="abs lbl" style="left:545px">Price</div>
<div class="abs field" style="left:587px;width:95px">$500k<svg width="11" height="7" viewBox="0 0 11 7"><path d="M1 1l4.5 4.5L10 1" stroke="#222" stroke-width="1.8" fill="none"/></svg></div>
<div class="abs lbl" style="left:693px">to</div>
<div class="abs field" style="left:716px;width:95px">$1000k<svg width="11" height="7" viewBox="0 0 11 7"><path d="M1 1l4.5 4.5L10 1" stroke="#222" stroke-width="1.8" fill="none"/></svg></div>
<div class="abs field" style="left:821px;width:77px;padding-left:7px">3 beds<svg width="11" height="7" viewBox="0 0 11 7"><path d="M1 1l4.5 4.5L10 1" stroke="#222" stroke-width="1.8" fill="none"/></svg></div>
<div class="abs field" style="left:909px;width:76px;padding-left:7px">2 baths<svg width="11" height="7" viewBox="0 0 11 7"><path d="M1 1l4.5 4.5L10 1" stroke="#222" stroke-width="1.8" fill="none"/></svg></div>
<div class="abs go"><svg width="18" height="18" viewBox="0 0 18 18"><circle cx="7" cy="7" r="5" stroke="#fff" stroke-width="2" fill="none"/><path d="M11 11l5 5" stroke="#fff" stroke-width="2.5"/></svg></div>

<div class="abs map" role="img" aria-label="Street map of the search area with lettered property markers"></div>

<div class="abs detail"></div>
<div class="abs photo" role="img" aria-label="Photo of the selected property's outdoor lounge terrace"></div>
<div class="abs arrow" style="left:801px"></div>
<div class="abs arrow" style="left:983px"></div>
<div class="abs d-title">Street Address</div>
<div class="abs d-line" style="top:362px"><b>$2,000,000</b> listing price</div>
<div class="abs d-line" style="top:381px"><b>2</b> beds</div>
<div class="abs d-line" style="top:381px;left:865px"><b>3</b> baths</div>
<div class="abs d-line" style="top:381px;left:950px">built in <b>2000</b></div>
<div class="abs d-line" style="top:400px"><b>2,000</b> Sq .Ft (600 / Sq .Ft)</div>
<div class="abs d-line" style="top:419px"><b>6,000</b> Sq .Ft Lot</div>
<div class="abs d-line" style="top:437px"><b>25 days</b> on market (#A1122334455)</div>
<div class="abs btn" style="left:791px;width:101px">details</div>
<div class="abs btn" style="left:921px;width:104px">visit home</div>

<div class="abs results">
<table>
<colgroup><col style="width:223px"><col style="width:138px"><col style="width:94px"><col style="width:67px"><col style="width:71px"><col style="width:101px"><col style="width:109px"><col style="width:93px"></colgroup>
<tr><th>Address ▾</th><th>City ▾</th><th>Price ▾</th><th>Beds ▾</th><th>Baths ▾</th><th>Sq .Ft ▾</th><th>$/Sq .Ft ▾</th><th>Days ▾</th></tr>
<tr><td>Street Address</td><td>Name of City</td><td>$2000,0000</td><td class="c">2</td><td class="c">2</td><td>2,000</td><td>6,000</td><td class="c">25</td></tr>
<tr class="active"><td>Street Address</td><td>Name of City</td><td>$2000,0000</td><td class="c">2</td><td class="c">2</td><td>2,000</td><td>6,000</td><td class="c">25</td></tr>
<tr><td>Street Address</td><td>Name of City</td><td>$2000,0000</td><td class="c">2</td><td class="c">2</td><td>2,000</td><td>6,000</td><td class="c">25</td></tr>
<tr><td>Street Address</td><td>Name of City</td><td>$2000,0000</td><td class="c">2</td><td class="c">2</td><td>2,000</td><td>6,000</td><td class="c">25</td></tr>
<tr><td>Street Address</td><td>Name of City</td><td>$2000,0000</td><td class="c">2</td><td class="c">2</td><td>2,000</td><td>6,000</td><td class="c">25</td></tr>
</table>
</div>
<div class="abs scroll"><i></i></div>

<div class="abs footer"></div>
<div class="abs f-h" style="left:145px">About Us</div>
<p class="abs about">Lorem Ipsum is simply dummy text of the printing and type setting industry. Lorem Ipsum has been the dummy text ever since the 1500s, Lorem the Ipsum has been ever since the 1500s, Lorem Ipsum is simply dummy text of the printing and type setting industry. Lorem Ipsum has been the dummy text ever since the 1500s, Lorem the Ipsum has been ever since the 1500s,</p>
<div class="abs f-h" style="left:771px">Connect With Us</div>
<div class="abs social" style="left:771px" aria-label="Social A">A</div>
<div class="abs social" style="left:818px" aria-label="Social B">B</div>
<div class="abs skyline" role="img" aria-label="City skyline silhouette scattered with map pins"></div>
</body>
</html>
```